Business Card for Web Design consulting firm

Business card designs for Web Design consulting firm

Target Market(s)

English speaking adults ages 30 - 60. Predominantly professional services eg. Doctor, Dentist

Industry/Entity Type

Consulting

Requirements
Must have
• Double sided card

```html
<!DOCTYPE html>
<html lang="en">
<head>
<meta charset="utf-8">
<title>Lumera – Business Card, Front and Back</title>
<link rel="stylesheet" href="https://fonts.googleapis.com/css2?family=Arimo:wght@400;700&display=swap">
<style>
  :root {
    --stage: #000000;
    --card: #f6f6f6;
    --card-light: #fcfcfc;
    --ink: #111111;
    --brand-dark: #3a4446;
    --brand-orange: #f7901e;
  }
  * { margin: 0; padding: 0; box-sizing: border-box; }
  html, body {
    width: 1200px;
    height: 425px;
    overflow: hidden;
    background: var(--stage);
  }
  body {
    position: relative;
    font-family: "Arimo", Arial, sans-serif;
    color: var(--ink);
  }
  .card {
    position: absolute;
    width: 545px;
    height: 273px;
    border-radius: 22px;
    overflow: hidden;
    background: linear-gradient(90deg, var(--card) 0%, var(--card-light) 55%, var(--card) 100%);
  }
  .card--front { left: 42px; top: 74px; }
  .card--back { left: 611px; top: 75px; }

  .card__wash {
    position: absolute;
    inset: 0;
  }
  .card--front .card__wash {
    background:
      radial-gradient(ellipse 60% 70% at 58% 55%, rgba(223,226,225,0.75), transparent 70%),
      radial-gradient(ellipse 40% 60% at 90% 50%, rgba(251,238,224,0.8), transparent 70%);
  }
  .card--back .card__wash {
    background:
      radial-gradient(ellipse 45% 70% at 30% 50%, rgba(223,226,225,0.7), transparent 70%),
      radial-gradient(ellipse 45% 70% at 62% 50%, rgba(251,238,224,0.8), transparent 70%);
  }

  .brand {
    position: absolute;
    left: 82px;
    top: 122px;
    display: flex;
    align-items: center;
    gap: 10px;
  }
  .brand__square {
    width: 20px;
    height: 20px;
    background: var(--brand-orange);
  }
  .brand__name {
    font-size: 37px;
    font-weight: 700;
    letter-spacing: 2px;
    color: var(--brand-dark);
    line-height: 1;
  }

  .divider {
    position: absolute;
    left: 0;
    top: 0;
  }

  .front-line {
    position: absolute;
    font-size: 26px;
    line-height: 1;
    white-space: nowrap;
  }
  .front-line--service { left: 297px; top: 87px; }
  .front-line--phone   { left: 325px; top: 118px; }
  .front-line--name    { left: 345px; top: 149px; }

  .back-line {
    position: absolute;
    left: 0;
    width: 100%;
    text-align: center;
    line-height: 1;
    white-space: nowrap;
  }
  .back-line--web { top: 98px; font-size: 26px; }
  .back-line--links { top: 150px; font-size: 26.5px; }
</style>
</head>
<body>
  <section class="card card--front" aria-label="Card front">
    <div class="card__wash" role="img" aria-label="Soft grey and cream background wash"></div>
    <div class="brand">
      <span class="brand__square"></span>
      <span class="brand__name">LUMERA</span>
    </div>
    <svg class="divider" width="545" height="273" viewBox="0 0 545 273" aria-hidden="true">
      <line x1="255" y1="66" x2="352" y2="190" stroke="#111111" stroke-width="1.4"/>
    </svg>
    <p class="front-line front-line--service">Web Design.</p>
    <p class="front-line front-line--phone">Phone number.</p>
    <p class="front-line front-line--name">Name amd tittle.</p>
  </section>

  <section class="card card--back" aria-label="Card back">
    <div class="card__wash" role="img" aria-label="Soft grey and cream background wash"></div>
    <p class="back-line back-line--web">www.website.com</p>
    <p class="back-line back-line--links">Contact • Services • Address.</p>
  </section>
</body>
</html>
```